Design new marketing postcard for mortgage loan applicants

I have provided a postcard recently designed as a possible guide for this project and have attached it. The new text is rough drafted and included. Please feel free to design outside of the old postcard or you can design close to it.

```html
<!DOCTYPE html>
<html lang="en">
<head>
<meta charset="utf-8">
<title>Cash Out Equity Loan Postcard</title>
<link rel="stylesheet" href="https://fonts.googleapis.com/css2?family=Open+Sans:ital,wdth,wght@0,75..100,400..800;1,75..100,400..800&family=Roboto:wght@500;700;900&display=swap">
<style>
  :root {
    --red: #e5202a;
    --navy-text: #15365c;
    --navy-band: #0e3a60;
    --navy-band-dark: #0a2a4a;
    --gold: #c4964e;
    --gold-light: #e7c787;
    --white: #ffffff;
    --ink: #111111;
  }
  html, body {
    margin: 0;
    padding: 0;
    width: 1200px;
    height: 822px;
    overflow: hidden;
    background: var(--white);
  }
  .postcard {
    position: relative;
    width: 1200px;
    height: 822px;
    background: var(--white);
    overflow: hidden;
  }
  .photo-area {
    position: absolute;
    left: 0;
    top: 0;
    width: 1200px;
    height: 640px;
  }
  .headline {
    position: absolute;
    left: 31px;
    top: 52px;
    margin: 0;
    font-family: "Open Sans", sans-serif;
    font-weight: 700;
    font-stretch: 86%;
    font-size: 60px;
    line-height: 1;
    color: var(--red);
    letter-spacing: 0.2px;
    white-space: nowrap;
  }
  .subhead {
    position: absolute;
    left: 32px;
    top: 118px;
    margin: 0;
    font-family: "Open Sans", sans-serif;
    font-weight: 400;
    font-size: 32px;
    line-height: 1;
    color: var(--red);
    letter-spacing: 5.6px;
    white-space: nowrap;
  }
  .benefits {
    position: absolute;
    left: 32px;
    top: 206px;
    margin: 0;
    padding: 0;
    list-style: none;
  }
  .benefits li {
    display: flex;
    align-items: center;
    height: 50.8px;
    font-family: "Open Sans", sans-serif;
    font-style: italic;
    font-weight: 600;
    font-size: 35px;
    color: var(--navy-text);
    white-space: nowrap;
  }
  .benefits .tick {
    width: 33px;
    height: 28px;
    margin-right: 15px;
    margin-top: 8px;
    flex: none;
  }
  .brand {
    position: absolute;
    left: 60px;
    top: 522px;
    height: 92px;
    display: flex;
    align-items: center;
  }
  .brand-mark {
    width: 22px;
    height: 22px;
    border-radius: 50%;
    background: var(--gold);
    margin-right: 14px;
  }
  .brand-name {
    font-family: "Open Sans", sans-serif;
    font-weight: 600;
    font-size: 22px;
    color: var(--navy-text);
    white-space: nowrap;
  }
  .license {
    position: absolute;
    left: 431px;
    top: 548px;
    margin: 0;
    font-family: "Roboto", sans-serif;
    font-weight: 500;
    font-size: 23px;
    color: var(--ink);
    white-space: nowrap;
  }
  .gold-rule {
    position: absolute;
    left: 0;
    top: 633px;
    width: 1200px;
    height: 6px;
    background: linear-gradient(90deg, var(--gold), var(--gold-light), var(--gold));
  }
  .call-band {
    position: absolute;
    left: 0;
    top: 639px;
    width: 1200px;
    height: 183px;
    background: linear-gradient(180deg, var(--navy-band), var(--navy-band-dark));
  }
  .call-label {
    position: absolute;
    left: 59px;
    top: 50px;
    width: 175px;
    height: 65px;
    background: var(--red);
    color: var(--white);
    font-family: "Roboto", sans-serif;
    font-weight: 700;
    font-size: 64px;
    line-height: 65px;
    text-align: center;
    letter-spacing: -1px;
  }
  .call-number {
    position: absolute;
    left: 258px;
    top: 6px;
    margin: 0;
    font-family: "Roboto", sans-serif;
    font-weight: 700;
    font-size: 134px;
    line-height: 1.2;
    color: var(--white);
    white-space: nowrap;
    letter-spacing: -1px;
  }
</style>
</head>
<body>
<main class="postcard">
  <svg class="photo-area" viewBox="0 0 1200 640" width="1200" height="640">
    <defs>
      <linearGradient id="photoTone" x1="0" y1="0" x2="1" y2="1">
        <stop offset="0" stop-color="#dfe8e6"/>
        <stop offset="0.35" stop-color="#d9b39c"/>
        <stop offset="0.7" stop-color="#8fa9c8"/>
        <stop offset="1" stop-color="#4f78ad"/>
      </linearGradient>
      <linearGradient id="arcGold" x1="0" y1="0" x2="0" y2="1">
        <stop offset="0" stop-color="#c08a45"/>
        <stop offset="0.5" stop-color="#f1d27f"/>
        <stop offset="1" stop-color="#b98540"/>
      </linearGradient>
    </defs>
    <path class="photo-fill" role="img" aria-label="Photo of a smiling couple embracing outdoors"
          d="M 805 0 L 1200 0 L 1200 633 L 700 633 Q 640 300 805 0 Z" fill="url(#photoTone)"/>
    <path class="gold-arc" d="M 752 0 L 805 0 Q 640 300 700 633 L 684 633 Q 610 300 752 0 Z" fill="url(#arcGold)"/>
  </svg>

  <h1 class="headline">CASH OUT EQULTY LOAN</h1>
  <p class="subhead">On Your Investment Property</p>

  <ul class="benefits">
    <li><svg class="tick" viewBox="0 0 33 28"><path d="M2 16 L12 26 L31 2" fill="none" stroke="var(--gold)" stroke-width="2.2"/></svg>Loan Based on Your Equity</li>
    <li><svg class="tick" viewBox="0 0 33 28"><path d="M2 16 L12 26 L31 2" fill="none" stroke="var(--gold)" stroke-width="2.2"/></svg>Fast Close</li>
    <li><svg class="tick" viewBox="0 0 33 28"><path d="M2 16 L12 26 L31 2" fill="none" stroke="var(--gold)" stroke-width="2.2"/></svg>No Income Qualitying</li>
    <li><svg class="tick" viewBox="0 0 33 28"><path d="M2 16 L12 26 L31 2" fill="none" stroke="var(--gold)" stroke-width="2.2"/></svg>Not Based on Credit Scores</li>
    <li><svg class="tick" viewBox="0 0 33 28"><path d="M2 16 L12 26 L31 2" fill="none" stroke="var(--gold)" stroke-width="2.2"/></svg>Competetive Rates</li>
  </ul>

  <div class="brand">
    <span class="brand-mark"></span>
    <span class="brand-name">Harborline Lending, Inc.</span>
  </div>
  <p class="license">NMLS #418503</p>

  <div class="gold-rule"></div>
  <section class="call-band">
    <div class="call-label">CALL</div>
    <p class="call-number">800-555-0147</p>
  </section>
</main>
</body>
</html>
```